Brightwell Systems Alliance Flyer for marketing and mailings

I need a Flyer Letter size and a Brochure for a Telecommunication Company. We provide Internet, Business phones, business solutions. It needs to informative but look clean and professional. The flyer needs to be Letter size

Target Market(s)

All Businesses that need internet, phones, business solutions

Industry/Entity Type

Technology / Telecom / Business solutions

Font styles to use
Sans Serif

Requirements
Must have
• Save up to 20% on internet and Voice Services / Needs to have my logo / “Get better a personal account manager and Rep” Needs to have pictures of communications (Business phones or internet representation somehow) Needs to have business solutions services offered "Audio and video calls with your teams and external, users Instant messaging and group chats, Presence status and geolocation synced across all user devices, Video conferencing with your teams and external users, Push notifications, new call popups and click2call, Fax & SMS to one or multiple people, Online access to corporate phonebooks, Screen sharing, Virtual Post-It and call-me-back notices, File transfer, Attendant Console, Control all user devices, Call activity stats and reporting, End-to-end encryption, Mobile apps, Voicemails and call recordings, CALL TRAFFIC ANALYSIS: MONITORING & REPORTING, CLOUD PBX, VIRTUAL PBX, HARDWARE PBX, Cyber Security" “BSA voice builds business phone systems specific to our customer's workflows!” “BSA offers relevant training to each account. By putting our customer workflows first, and understanding their business concepts, our voice engineers can design, implement and train our end users. This behavior helps move business forward for each client, creating a true partnership that is focused on outcomes.” Must have our info: 4825 Marlow Ste. 3100 Denver, CO 80419 / (303) 555-0187 / https://www.brightwellsystems.example/ need QR scan / Email: sales@brightwellsystems.example EQUIPMENT INSTALLATION Security Camera TVs and TV Mounts Sound Systems Wifi Access WIRING AND DEVICE INSTALLATION All types of audio, video, data, and voice cabling CCTV Alarms and Cameras Wifi Access Points
Nice to have
• Pictures are for inspiration, try to keep colors that match logo
Should not have
• Try not to make it too cluttered

```html
<!DOCTYPE html>
<html lang="en">
<head>
<meta charset="utf-8">
<title>Brightwell Systems Alliance – Flyer</title>
<link href="https://fonts.googleapis.com/css2?family=Cabin:wght@400;500;600;700&family=Montserrat:wght@600;700;800&family=Montserrat+Alternates:wght@600;700&display=swap" rel="stylesheet">
<style>
  :root{
    --page-bg:#3e6ea8;
    --paper:#fbfcfe;
    --brand-blue:#2b7cf0;
    --brand-blue-dark:#1f5fc2;
    --band-start:#2d78ff;
    --band-end:#45a6e6;
    --ink:#333638;
    --ink-soft:#3a3d40;
    --ring:#d4e6fa;
    --ring-faint:#edf3fa;
    --cell:#ffffff;
    --link:#1a5cb8;
  }
  *{margin:0;padding:0;box-sizing:border-box}
  html,body{width:1200px;height:1200px;overflow:hidden}
  body{background:var(--page-bg);position:relative;font-family:"Cabin",sans-serif}
  .flyer{position:absolute;left:136px;top:0;width:928px;height:1200px;background:var(--paper);overflow:hidden}
  .decor{position:absolute;inset:0}
  .brand{position:absolute;left:90px;top:78px;width:190px;text-align:center}
  .brand-mark{width:40px;height:40px;border-radius:50%;background:var(--brand-blue);margin:0 auto 10px}
  .brand-name{font-family:"Cabin",sans-serif;font-weight:600;font-size:15px;color:var(--brand-blue-dark);letter-spacing:.3px;line-height:1.2}
  .hero-photo{position:absolute;left:83px;top:216px;width:400px;height:365px;border-radius:18px;
    background:radial-gradient(ellipse at 45% 45%,#5b6672 0%,#2d3238 45%,#a9b8c8 80%,rgba(240,244,250,0) 100%)}
  .offer-lead{position:absolute;left:521px;top:140px;font-family:"Montserrat Alternates",sans-serif;font-weight:700;font-size:52px;color:var(--brand-blue);letter-spacing:1px}
  .offer-figure{position:absolute;left:516px;top:186px;font-family:"Montserrat",sans-serif;font-weight:800;font-size:152px;line-height:1;color:var(--brand-blue);letter-spacing:-3px}
  .offer-scope{position:absolute;left:521px;top:330px;font-family:"Montserrat",sans-serif;font-weight:700;font-size:38px;line-height:40px;color:var(--ink)}
  .offer-rule{position:absolute;left:521px;top:445px;width:316px;height:2px;background:var(--ink)}
  .offer-note{position:absolute;left:521px;top:478px;font-family:"Montserrat Alternates",sans-serif;font-weight:600;font-size:25px;line-height:27px;color:var(--ink-soft)}
  .services-title{position:absolute;left:0;width:928px;top:596px;text-align:center;font-family:"Montserrat",sans-serif;font-weight:600;font-size:27px;color:var(--ink)}
  .services{position:absolute;left:96px;top:658px;width:734px;display:grid;grid-template-columns:repeat(6,1fr);grid-template-rows:87px 87px 87px;gap:6px 4px}
  .service{background:var(--cell);box-shadow:0 1px 4px rgba(40,60,90,.12);display:flex;flex-direction:column;align-items:center;justify-content:center;text-align:center;font-size:12px;line-height:13px;color:#222;padding:0 8px;font-weight:500}
  .service.wide{grid-column:span 2}
  .service .label{color:var(--brand-blue-dark);font-weight:600;margin-bottom:8px}
  .band{position:absolute;left:0;top:971px;width:928px;height:148px;display:grid;grid-template-columns:321px 326px 281px;background:linear-gradient(90deg,var(--band-start),var(--band-end))}
  .band-col{color:#fff;text-align:center;padding-top:22px}
  .band-col+.band-col{background:linear-gradient(90deg,var(--band-start),var(--band-end))}
  .band-col h3{font-size:13px;font-weight:700;letter-spacing:.2px}
  .band-col .dash{width:48px;height:2px;background:#fff;margin:10px auto 8px;opacity:.9}
  .band-col p{font-size:15px;font-weight:700;line-height:18px}
  .band-accent{position:absolute;top:967px;height:4px;width:133px;background:var(--brand-blue-dark)}
  .contact{padding-top:25px;text-align:left;padding-left:20px}
  .contact h3{text-align:center;margin-bottom:10px}
  .contact-row{display:flex;align-items:flex-start;gap:8px;font-size:13px;font-weight:700;line-height:14px;margin-bottom:8px}
  .contact-row svg{flex:none}
  .learn-more{position:absolute;left:237px;top:1132px;width:448px;height:35px;border-radius:18px;background:#fff;box-shadow:0 1px 6px rgba(40,60,90,.08);display:flex;align-items:center;justify-content:center;font-size:15px;font-weight:700;color:var(--link)}
</style>
</head>
<body>
  <main class="flyer">
    <svg class="decor" width="928" height="1200" aria-hidden="true">
      <circle cx="210" cy="95" r="255" fill="none" stroke="var(--ring)" stroke-width="50" opacity=".85"/>
      <circle cx="930" cy="705" r="150" fill="none" stroke="var(--ring-faint)" stroke-width="38"/>
    </svg>

    <header class="brand">
      <div class="brand-mark"></div>
      <div class="brand-name">BRIGHTWELL SYSTEMS ALLIANCE</div>
    </header>

    <div class="hero-photo" role="img" aria-label="Business desk phones, two-way radio, handheld scanner and video-conferencing screens grouped together"></div>

    <div class="offer-lead">enjoy</div>
    <div class="offer-figure">20%</div>
    <div class="offer-scope">on internet and<br>Voice Services</div>
    <div class="offer-rule"></div>
    <div class="offer-note">Get better a personal<br>account manager and Rep</div>

    <h2 class="services-title">Business Solutions Services We offer:</h2>
    <section class="services">
      <div class="service">Audio and video calls with your teams and external</div>
      <div class="service">users Instant messaging and group chats</div>
      <div class="service">Presence status and geolocation synced across all user devices</div>
      <div class="service">Video conferencing with your teams and external users</div>
      <div class="service">Push notifications, new call popups and click2call</div>
      <div class="service">Fax &amp; SMS to one or multiple people, Online access to corporate phonebooks</div>
      <div class="service">Screen sharing</div>
      <div class="service">Virtual Post-It and call-me-back notices</div>
      <div class="service">File transfer</div>
      <div class="service">Attendant Console</div>
      <div class="service">Control all user devices</div>
      <div class="service">Call activity stats and reporting</div>
      <div class="service">End-to-end encryption</div>
      <div class="service">Mobile apps</div>
      <div class="service">Voicemails and call recordings</div>
      <div class="service">Cyber Security</div>
      <div class="service wide"><span class="label">CALL TRAFFIC ANALYSIS:</span>Monitoring &amp; Reporting,<br>Cloud Pbx, Virtual Pbx, Hardware Pbx,</div>
    </section>

    <div class="band-accent" style="left:92px"></div>
    <div class="band-accent" style="left:412px"></div>
    <div class="band-accent" style="left:730px"></div>
    <section class="band">
      <div class="band-col">
        <h3>EQUIPMENT INSTALLATION</h3>
        <div class="dash"></div>
        <p>Security Camera<br>TVs and TV Mounts<br>Sound Systems<br>Wifi Access</p>
      </div>
      <div class="band-col">
        <h3>WIRING AND DEVICE INSTALLATION</h3>
        <div class="dash"></div>
        <p>All types of audio,<br>video, data, and voice cabling<br>CCTV, Alarms and Cameras<br>Wifi Access Points</p>
      </div>
      <div class="band-col contact">
        <h3>CONTACT INFO:</h3>
        <div class="contact-row">
          <svg width="16" height="13" viewBox="0 0 16 13"><rect x="1" y="1" width="14" height="11" fill="none" stroke="#fff" stroke-width="2"/><path d="M1 1l7 6 7-6" fill="none" stroke="#fff" stroke-width="2"/></svg>
          <span>sales@brightwellsystems.example</span>
        </div>
        <div class="contact-row">
          <svg width="14" height="17" viewBox="0 0 14 17"><path d="M7 1a6 6 0 0 1 6 6c0 4-6 9-6 9S1 11 1 7a6 6 0 0 1 6-6z" fill="#fff"/><circle cx="7" cy="7" r="2.3" fill="var(--band-end)"/></svg>
          <span>4825 Marlow Ste. 3100 Denver,<br>CO 80419</span>
        </div>
        <div class="contact-row">
          <svg width="16" height="16" viewBox="0 0 16 16"><circle cx="8" cy="8" r="7" fill="none" stroke="#fff" stroke-width="1.6"/><path d="M5.2 4.2l1.4-.3.9 2-1 .8c.5 1.1 1.4 2 2.5 2.5l.8-1 2 .9-.3 1.4c-3.5.3-6.6-2.8-6.3-6.3z" fill="#fff"/></svg>
          <span>(303) 555-0187</span>
        </div>
      </div>
    </section>

    <a class="learn-more">Learn more:&nbsp; https://www.brightwellsystems.example/</a>
  </main>
</body>
</html>
```